Healthcare IT company looking for business card design

We develop IT systems for healthcare that significantly reduces cost and improves quality.

We want a business card design that is professional and clean, and using the colors in our logo.

Doctors and decision makers in the healthcare industry

Healthcare

It should include
Name and title, address, telephone

Torvald Eskberg, CEO
+46 712 480517
torvald@velpamo.se

Serif

0355a3
ed282f

• Clean design
• Professional feel
• N/A
• N/A

```html
<!DOCTYPE html>
<html lang="en">
<head>
<meta charset="utf-8">
<title>Velpamo business card</title>
<link rel="stylesheet" href="https://fonts.googleapis.com/css2?family=Ubuntu:wght@400;500;700&display=swap">
<style>
  :root {
    --brand-blue: #0355a3;
    --brand-red: #ed282f;
    --card-white: #ffffff;
    --backdrop: #1c1c1e;
    --ink: #2a2a2a;
  }
  * { margin: 0; padding: 0; box-sizing: border-box; }
  html, body {
    width: 1200px; height: 900px; overflow: hidden;
    background: var(--backdrop);
    font-family: "Ubuntu", Arial, sans-serif;
  }
  .canvas { position: relative; width: 1200px; height: 900px; }

  .card {
    position: absolute;
    width: 560px; height: 320px;
    overflow: hidden;
    box-shadow: 0 10px 30px rgba(0,0,0,.55);
  }
  .card--front { left: 70px; top: 70px; background: var(--card-white); }
  .card--back  { left: 570px; top: 500px; background: var(--brand-blue); }

  .accent-band {
    position: absolute; top: 0; bottom: 0; width: 70px;
    background: var(--brand-red);
  }
  .card--front .accent-band { right: 0; }
  .card--back .accent-band { left: 0; }

  .wordmark {
    position: absolute;
    font-weight: 700;
    letter-spacing: -1px;
    line-height: 1;
  }
  .card--front .wordmark { left: 44px; top: 60px; font-size: 62px; color: var(--brand-blue); }
  .card--back .wordmark  { left: 180px; top: 128px; font-size: 66px; color: var(--card-white); }

  .holder { position: absolute; left: 44px; top: 170px; }
  .holder__name {
    font-size: 17px; font-weight: 700; color: var(--brand-blue);
    text-transform: uppercase; letter-spacing: .3px;
  }
  .holder__title { font-size: 14px; color: var(--brand-red); margin-top: 4px; }

  .contact-list { position: absolute; left: 44px; top: 236px; list-style: none; }
  .contact-list li {
    display: flex; align-items: center; gap: 8px;
    font-size: 14px; color: var(--ink); height: 20px;
  }
  .contact-icon {
    width: 16px; height: 16px; background: var(--brand-blue);
    display: inline-flex; align-items: center; justify-content: center;
  }
  .contact-icon svg { width: 12px; height: 12px; }
</style>
</head>
<body>
<main class="canvas">

  <section class="card card--front" aria-label="Card front">
    <div class="wordmark">Velpamo</div>
    <div class="holder">
      <p class="holder__name">Torvald Eskberg</p>
      <p class="holder__title">Ceo</p>
    </div>
    <ul class="contact-list">
      <li>
        <span class="contact-icon">
          <svg viewBox="0 0 12 12"><path d="M3 1.5 L4.6 3.4 L3.7 4.6 Q4.8 6.9 7.2 8.2 L8.5 7.3 L10.5 8.9 L9.4 10.5 Q5.5 10.3 2.3 6.2 Q1 4 1.6 2.6 Z" fill="#fff"/></svg>
        </span>+46 712 480517
      </li>
      <li>
        <span class="contact-icon">
          <svg viewBox="0 0 12 12"><rect x="1.5" y="3" width="9" height="6.5" fill="none" stroke="#fff" stroke-width="1.2"/><path d="M1.5 3 L6 6.8 L10.5 3" fill="none" stroke="#fff" stroke-width="1.2"/></svg>
        </span>torvald@velpamo.se
      </li>
      <li>
        <span class="contact-icon">
          <svg viewBox="0 0 12 12"><circle cx="6" cy="6" r="4.5" fill="none" stroke="#fff" stroke-width="1.1"/><ellipse cx="6" cy="6" rx="2" ry="4.5" fill="none" stroke="#fff" stroke-width="1"/><path d="M1.5 6 H10.5" stroke="#fff" stroke-width="1"/></svg>
        </span>www.velpamo.se
      </li>
    </ul>
    <div class="accent-band"></div>
  </section>

  <section class="card card--back" aria-label="Card back">
    <div class="accent-band"></div>
    <div class="wordmark">Velpamo</div>
  </section>

</main>
</body>
</html>
```